Art for parenting podcast with straight/direct talk...no fluff here! "Plain Answers for Families"

I need an image that will not look fluffy or soft. A no-nonsense look. This is not a 'I love parenting' podcast. It is for frustrated parents who don't know what to do. The name is 'Plain Answers for Families'. The design should, therefore, NOT have hearts and flowers but, instead, look clean and direct. My logo has shades of blue so that would be nice. I have done this work for over 30 years and am well-degreed so would like the design to look stable/established. I have attached my company's logo.

Target Market(s)

Frustrated parents of children - age birth to 20

Industry/Entity Type

Coaching/Counseling for parents

Font styles to use
Serif
Sans Serif

Colors
0054AA
0677BA
7BADD7
CADEEF
E8F1F8

Requirements
Must have
• A look that is clean/bold/direct and professional. Serious.
Nice to have
• If it looks good, my name with my degrees behind my name. MS, MEd. Another thought would be to have a background image of a frustrated parent. Not sure if that would be good or look too busy.
Should not have
• Flowers, fluff, soft appearance, pinks, light colors

```html
<!DOCTYPE html>
<html lang="en">
<head>
<meta charset="utf-8">
<title>Plain Answers for Families – Podcast Cover</title>
<link rel="stylesheet" href="https://fonts.googleapis.com/css2?family=Bebas+Neue&display=swap">
<style>
  :root {
    --page: #ffffff;
    --brand-blue: #0368AF;
    --brand-blue-deep: #0360A8;
    --glow: #5E9DD4;
    --mid-blue: #0677BA;
    --pale-blue: #CADEEF;
    --white: #ffffff;
    --shadow-navy: #131127;
  }
  html, body {
    margin: 0;
    width: 1200px;
    height: 1200px;
    overflow: hidden;
    background: var(--page);
  }
  .canvas {
    position: relative;
    width: 1200px;
    height: 1200px;
  }
  .cover {
    position: absolute;
    top: 351px;
    width: 507px;
    height: 507px;
    background:
      radial-gradient(circle at 76% 66%, var(--glow) 0%, var(--mid-blue) 26%, var(--brand-blue) 52%, var(--brand-blue-deep) 100%);
    overflow: hidden;
    font-family: "Bebas Neue", "Arial Narrow", sans-serif;
  }
  .cover--left { left: 70px; }
  .cover--right { left: 630px; }

  .cover__frame {
    position: absolute;
    inset: 15px;
    border: 4px solid var(--white);
    pointer-events: none;
    z-index: 3;
  }

  .cover__figure {
    position: absolute;
    left: 318px;
    top: 234px;
    width: 171px;
    height: 254px;
    background: linear-gradient(180deg, #1a1838 0%, var(--shadow-navy) 60%);
    border-radius: 60px 40px 0 0;
    z-index: 1;
  }

  .title {
    position: absolute;
    left: 39px;
    top: 62px;
    margin: 0;
    font-weight: 400;
    font-size: 104px;
    line-height: 86px;
    color: var(--white);
    z-index: 2;
    letter-spacing: 0;
  }
  .title__line { display: block; white-space: nowrap; }
  .title__line--accent { color: var(--pale-blue); }
  .title__badge {
    display: inline-block;
    vertical-align: top;
    width: 80px;
    height: 80px;
    margin: 3px 0 0 10px;
    border-radius: 50%;
    background: var(--white);
    color: var(--brand-blue);
    font-size: 50px;
    line-height: 84px;
    text-align: center;
  }

  .podcast-label {
    position: absolute;
    left: 0;
    width: 368px;
    top: 330px;
    text-align: center;
    font-size: 43px;
    line-height: 1;
    color: var(--white);
    z-index: 2;
  }

  .brand {
    position: absolute;
    left: 84px;
    width: 200px;
    top: 390px;
    text-align: center;
    color: var(--white);
    z-index: 2;
  }
  .cover--right .brand { top: 396px; }
  .brand__dot {
    display: block;
    width: 26px;
    height: 26px;
    margin: 0 auto 6px;
    border-radius: 50%;
    background: var(--white);
  }
  .brand__name {
    font-size: 20px;
    line-height: 1;
    letter-spacing: 1px;
  }
</style>
</head>
<body>
<div class="canvas">

  <section class="cover cover--left">
    <div class="cover__figure" role="img" aria-label="Dark silhouette of a frustrated parent with head bowed"></div>
    <h1 class="title">
      <span class="title__line">PLAIN</span>
      <span class="title__line title__line--accent">ANSWERS<span class="title__badge">FOR</span></span>
      <span class="title__line">FAMILIES</span>
    </h1>
    <div class="podcast-label">PODCAST</div>
    <div class="brand">
      <span class="brand__dot"></span>
      <div class="brand__name">STEADY GROUND COACHING</div>
    </div>
    <div class="cover__frame"></div>
  </section>

  <section class="cover cover--right">
    <div class="cover__figure" role="img" aria-label="Dark silhouette of a frustrated parent with head bowed"></div>
    <h1 class="title">
      <span class="title__line">PLAIN</span>
      <span class="title__line title__line--accent">ANSWERS<span class="title__badge">FOR</span></span>
      <span class="title__line">FAMILIES</span>
    </h1>
    <div class="podcast-label">PODCAST</div>
    <div class="brand">
      <span class="brand__dot"></span>
      <div class="brand__name">STEADY GROUND COACHING</div>
    </div>
    <div class="cover__frame"></div>
  </section>

</div>
</body>
</html>
```